BRISKA sparkling water needs new artwork! Based in Southern California

"Briska" is a new sparkling water company based in Southern California that offers refreshing flavors (lime, cherry, & mango) with B vitamins and antioxidants.

We would like to see packaging designs for standard 12oz cans for each of the three flavors.
Our initial preference is to have individual artwork for each flavor.

Attached are examples of competitors' designs.
Updates

We are extending the deadline for the Thanksgiving Holiday. Thank you all for your contributions.

```html
<!DOCTYPE html>
<html lang="en">
<head>
<meta charset="utf-8">
<title>Briska Sparkling Water – Can Labels</title>
<link href="https://fonts.googleapis.com/css2?family=Josefin+Sans:wght@400;600;700&display=swap" rel="stylesheet">
<style>
  :root {
    --navy: #262a4a;
    --sky: #8fd0f2;
    --sky-deep: #5cb8ea;
    --stage-top: #ffffff;
    --stage-bottom: #8dbde2;
    --cherry: #e8336b;
    --cherry-deep: #c81a4e;
    --lime: #5cc04a;
    --lime-deep: #2f9a3a;
    --mango: #ffc93a;
    --mango-deep: #f7a21d;
    --white: #ffffff;
  }
  * { margin: 0; padding: 0; box-sizing: border-box; }
  html, body { width: 1200px; height: 960px; overflow: hidden; }
  body {
    font-family: "Josefin Sans", sans-serif;
    background: linear-gradient(180deg, var(--stage-top) 0%, var(--stage-top) 45%, var(--stage-bottom) 100%);
    position: relative;
  }
  .label {
    position: absolute;
    top: 200px;
    width: 266px;
    height: 520px;
    border-radius: 10px;
    overflow: hidden;
  }
  .label--cherry { left: 160px; --flavor: var(--cherry); --flavor-deep: var(--cherry-deep); }
  .label--lime   { left: 476px; --flavor: var(--lime);   --flavor-deep: var(--lime-deep); }
  .label--mango  { left: 800px; --flavor: var(--mango);  --flavor-deep: var(--mango-deep); }

  .label__field {
    position: absolute; inset: 0;
    background: linear-gradient(180deg,
      var(--sky) 0%, var(--sky-deep) 38%,
      var(--flavor) 46%, var(--flavor-deep) 100%);
  }
  .label__badge {
    position: absolute;
    left: 50%; top: 208px;
    width: 268px; height: 268px;
    margin: -134px 0 0 -134px;
    border-radius: 50%;
    background: var(--white);
    display: flex; align-items: center; justify-content: center;
  }
  .label__brand {
    font-weight: 700;
    font-size: 38px;
    letter-spacing: 4px;
    color: var(--navy);
    padding-top: 6px;
  }
  .label__flavor-band {
    position: absolute; left: 0; right: 0; top: 350px; height: 36px;
    background: var(--flavor-deep);
    opacity: .9;
    display: flex; align-items: center; justify-content: center;
  }
  .label__flavor {
    color: var(--white);
    font-weight: 600;
    font-size: 19px;
    letter-spacing: 3px;
    padding-top: 4px;
  }
  .label__claims {
    position: absolute; left: 0; right: 0; top: 390px; height: 38px;
    background: rgba(255,255,255,.72);
    text-align: center;
    color: var(--navy);
    font-size: 10.5px;
    font-weight: 600;
    letter-spacing: 1.6px;
    line-height: 14px;
    padding-top: 6px;
  }
  .label__size {
    position: absolute; left: 0; right: 0; top: 462px;
    text-align: center;
    color: var(--white);
    font-size: 12px;
    letter-spacing: 2px;
  }
</style>
</head>
<body>
  <section class="label label--cherry">
    <div class="label__field" role="img" aria-label="Sky-blue to cherry-red gradient with water droplets"></div>
    <div class="label__badge"><span class="label__brand">BRISKA</span></div>
    <div class="label__flavor-band"><span class="label__flavor">CHERRY</span></div>
    <div class="label__claims">WITH B VITAMINS<br>AND ANTIOXIDANTS</div>
    <div class="label__size">12 OZ</div>
  </section>

  <section class="label label--lime">
    <div class="label__field" role="img" aria-label="Sky-blue to lime-green gradient with water droplets"></div>
    <div class="label__badge"><span class="label__brand">BRISKA</span></div>
    <div class="label__flavor-band"><span class="label__flavor">LIME</span></div>
    <div class="label__claims">WITH B VITAMINS<br>AND ANTIOXIDANTS</div>
    <div class="label__size">12 OZ</div>
  </section>

  <section class="label label--mango">
    <div class="label__field" role="img" aria-label="Sky-blue to mango-yellow gradient with water droplets"></div>
    <div class="label__badge"><span class="label__brand">BRISKA</span></div>
    <div class="label__flavor-band"><span class="label__flavor">MANGO</span></div>
    <div class="label__claims">WITH B VITAMINS<br>AND ANTIOXIDANTS</div>
    <div class="label__size">12 OZ</div>
  </section>
</body>
</html>
```